Brookfarrow Osteopathy and dry needling business card

Business card for Brookfarrow Osteopathy and Dry Needling.

Industry/Entity Type

Health

Contact Information for Business Card

I do not have a phone number yet. I also do not have an email address yet. The physical address is: 48 Lower Crane Street Brookfarrow The website is: www.brookfarrowosteosteopathy.example My details are: Dr Martin Pellowe, Osteopath (B.Clin.Sci (Ost) M.Ost BSC ECON (Hons)

Colors
0094D4
00A9DD
6FCCEA
C7EBF8
E9F6FB

Requirements
Must have
• logo on the back
Nice to have
• Maybe a space for me to write an appointment time and date on the card.

```html
<!DOCTYPE html>
<html lang="en">
<head>
<meta charset="utf-8">
<title>Brookfarrow Osteopathy and Dry Needling – Business Card</title>
<link rel="stylesheet" href="https://fonts.googleapis.com/css2?family=Arimo:wght@400;700&display=swap">
<style>
  :root {
    --page-bg: #ececec;
    --card-white: #ffffff;
    --card-dark: #282828;
    --brand-blue: #0094d4;
    --brand-sky: #00a9dd;
    --accent-orange: #f7931e;
    --ink: #111111;
    --gold: #c9a94a;
  }
  * { box-sizing: border-box; margin: 0; padding: 0; }
  html, body {
    width: 1200px; height: 1199px; overflow: hidden;
    background: var(--page-bg);
    font-family: "Arimo", Arial, sans-serif;
    color: var(--ink);
  }
  .canvas { position: relative; width: 1200px; height: 1199px; }

  .card {
    position: absolute;
    border-radius: 26px;
    overflow: hidden;
    box-shadow: 0 10px 24px rgba(0,0,0,0.12);
  }
  .card-front {
    left: 246px; top: 157px; width: 725px; height: 413px;
    background: var(--card-white);
  }
  .front-band {
    position: absolute; right: 0; bottom: 0; width: 430px; height: 27px;
    background: var(--brand-blue);
    border-top-left-radius: 30px;
  }

  .brand-seal {
    position: absolute; left: 62px; top: 103px;
    width: 216px; height: 216px;
    border: 3px solid var(--brand-sky);
    border-radius: 50%;
    display: flex; align-items: center; justify-content: center;
    text-align: center; padding: 30px;
  }
  .brand-name {
    font-weight: 700; font-size: 21px; line-height: 1.25;
    color: var(--brand-sky); text-transform: uppercase; letter-spacing: 0.5px;
  }

  .details { position: absolute; left: 335px; top: 78px; }
  .person-name {
    font-weight: 700; font-size: 25px; color: var(--accent-orange);
    letter-spacing: 0.3px;
  }
  .credentials { font-weight: 700; font-size: 12px; margin-top: 9px; }
  .address { font-size: 18px; margin-top: 32px; }
  .contact-list { list-style: none; margin-top: 44px; }
  .contact-list li {
    display: flex; align-items: center; gap: 10px;
    font-size: 18px; height: 28.5px;
  }
  .contact-icon { width: 20px; height: 20px; flex: none; }

  .card-back {
    left: 227px; top: 649px; width: 737px; height: 419px;
    background: var(--card-dark);
  }
  .back-mark {
    position: absolute; left: 258px; top: 46px;
    width: 224px; height: 224px;
    border: 3px solid var(--gold); border-radius: 50%;
    display: flex; align-items: center; justify-content: center;
    text-align: center; padding: 30px;
  }
  .back-mark .brand-name { color: var(--gold); }
  .appointment-field {
    position: absolute; left: 31px; top: 329px;
    width: 681px; height: 66px;
    background: var(--card-white); border-radius: 17px;
    padding: 12px 16px;
    font-size: 18px;
  }
</style>
</head>
<body>
<div class="canvas">

  <section class="card card-front" aria-label="Business card front">
    <div class="brand-seal">
      <span class="brand-name">Brookfarrow Osteopathy and Dry Needling</span>
    </div>

    <div class="details">
      <h1 class="person-name">DR MARTIN PELLOWE</h1>
      <p class="credentials">Osteopath (B.Clin.Sci (Ost) M.Ost BSC ECON (Hons)</p>
      <p class="address">48 Lower Crane Street Brookfarrow</p>
      <ul class="contact-list">
        <li>
          <svg class="contact-icon" viewBox="0 0 20 20" aria-hidden="true">
            <circle cx="10" cy="10" r="8.8" fill="none" stroke="var(--brand-blue)" stroke-width="1.4"/>
            <path d="M7 5.5l1.6 2.4-1 1a6 6 0 0 0 3.5 3.5l1-1 2.4 1.6-.9 1.6c-3.8.2-7.8-3.8-7.6-7.6z" fill="var(--brand-blue)"/>
          </svg>
          555 010 0142
        </li>
        <li>
          <svg class="contact-icon" viewBox="0 0 20 20" aria-hidden="true">
            <circle cx="10" cy="10" r="8.8" fill="none" stroke="var(--brand-blue)" stroke-width="1.4"/>
            <rect x="7" y="4.8" width="6" height="10.4" rx="1.2" fill="none" stroke="var(--brand-blue)" stroke-width="1.3"/>
            <circle cx="10" cy="13.3" r="0.7" fill="var(--brand-blue)"/>
          </svg>
          555 010 0187
        </li>
        <li>
          <svg class="contact-icon" viewBox="0 0 20 20" aria-hidden="true">
            <circle cx="10" cy="10" r="8.8" fill="none" stroke="var(--brand-blue)" stroke-width="1.4"/>
            <rect x="5.2" y="6.8" width="9.6" height="6.4" rx="0.8" fill="var(--brand-blue)"/>
            <path d="M5.5 7.2l4.5 3.3 4.5-3.3" fill="none" stroke="#fff" stroke-width="0.9"/>
          </svg>
          info@brookfarrow.example
        </li>
        <li>
          <svg class="contact-icon" viewBox="0 0 20 20" aria-hidden="true">
            <circle cx="10" cy="10" r="8.8" fill="none" stroke="var(--brand-blue)" stroke-width="1.4"/>
            <circle cx="10" cy="10" r="5" fill="none" stroke="var(--brand-blue)" stroke-width="1.1"/>
            <ellipse cx="10" cy="10" rx="2.2" ry="5" fill="none" stroke="var(--brand-blue)" stroke-width="1"/>
            <path d="M5 10h10" stroke="var(--brand-blue)" stroke-width="1"/>
          </svg>
          www.brookfarrowosteosteopathy.example
        </li>
      </ul>
    </div>

    <div class="front-band"></div>
  </section>

  <section class="card card-back" aria-label="Business card back">
    <div class="back-mark">
      <span class="brand-name">Brookfarrow Osteopathy and Dry Needling</span>
    </div>
    <div class="appointment-field">Appointment</div>
  </section>

</div>
</body>
</html>
```